Thank You Card

I'm looking for a thank you card design using our logo and other graphics. We are an essential business and our employees (Electricians) have done an incredible job staying healthy and safe during the COVID-19 pandemic, I want to send each a thank you card.

```html
<!DOCTYPE html>
<html lang="en">
<head>
<meta charset="utf-8">
<title>Thank You Card</title>
<link href="https://fonts.googleapis.com/css2?family=Montserrat:wght@500;800&family=Roboto+Slab:wght@800&display=swap" rel="stylesheet">
<style>
  :root {
    --page: #ececec;
    --navy: #0f2a8c;
    --navy-deep: #0b1f66;
    --red: #e3162b;
    --ice: #eef6fc;
    --sky: #b9dcf2;
    --ink: #1c1c24;
  }
  html, body {
    margin: 0;
    width: 1200px;
    height: 1200px;
    overflow: hidden;
    background: var(--page);
  }
  .card {
    position: absolute;
    left: 75px;
    top: 300px;
    width: 1050px;
    height: 600px;
    overflow: hidden;
    background: var(--ice);
    box-shadow: 0 6px 24px rgba(0,0,0,0.15);
  }
  .card-backdrop {
    position: absolute;
    inset: 0;
    background:
      radial-gradient(ellipse at 35% 60%, #ffffff 0%, rgba(255,255,255,0) 55%),
      linear-gradient(135deg, var(--sky) 0%, var(--ice) 45%, #dcecf8 100%);
  }
  .worker-photo {
    position: absolute;
    right: 0;
    top: 0;
    width: 380px;
    height: 440px;
    background:
      linear-gradient(200deg, #1f2d66 0%, #2a3a78 30%, #c9d5e3 60%, #e9eef4 100%);
  }
  .accent-rule {
    position: absolute;
    left: 650px;
    top: 220px;
    width: 5px;
    height: 200px;
    background: var(--red);
  }
  .headline {
    position: absolute;
    left: 150px;
    top: 250px;
    margin: 0;
    font-family: "Roboto Slab", serif;
    font-weight: 800;
    font-size: 84px;
    line-height: 1;
    color: var(--navy);
    white-space: nowrap;
  }
  .message {
    position: absolute;
    left: 150px;
    top: 352px;
    width: 470px;
    margin: 0;
    font-family: "Montserrat", sans-serif;
    font-weight: 500;
    font-size: 17px;
    line-height: 1.4;
    color: var(--ink);
  }
  .message .line { display: block; white-space: nowrap; }
  .message .highlight { color: var(--red); }
  .band {
    position: absolute;
    background: var(--navy);
  }
  .band-left { left: 0; top: 548px; width: 105px; height: 52px; }
  .band-right { left: 345px; top: 440px; width: 705px; height: 60px; }
  .brand {
    position: absolute;
    left: 125px;
    top: 505px;
    display: flex;
    align-items: center;
    gap: 10px;
    font-family: "Montserrat", sans-serif;
    font-weight: 800;
    font-size: 22px;
    line-height: 1.05;
    color: var(--navy-deep);
    text-transform: uppercase;
  }
  .brand-dot {
    width: 22px;
    height: 22px;
    border-radius: 50%;
    background: var(--red);
    flex: none;
  }
</style>
</head>
<body>
  <article class="card">
    <div class="card-backdrop" role="img" aria-label="Soft light blue background with floating bubbles and virus particles"></div>
    <div class="worker-photo" role="img" aria-label="Photo of a healthcare worker in a navy scrub cap adjusting a surgical mask"></div>
    <div class="accent-rule"></div>
    <div class="band band-right"></div>
    <div class="band band-left"></div>

    <h1 class="headline">Thank You</h1>
    <p class="message">
      <span class="line">We are an essential business and our employees</span>
      <span class="line">(Electricians) have done an incredible job staying</span>
      <span class="line">healthy and safe during the <span class="highlight">COVID-19</span> pandemic</span>
    </p>

    <div class="brand">
      <span class="brand-dot"></span>
      <span>Brightline Electric<br>Incorporated</span>
    </div>
  </article>
</body>
</html>
```